Real Estate Business Cards

Looking for a clean, sharp and professional look for our Real Estate investment Fund that invests in Multi Family Apartment buildings.

Target Market(s)

Real Estate Fund

Industry/Entity Type

Real Estate

Contact Information for Business Card

Company Description: Real Estate Investment Fund
Company Name: RKW Holdings
Name: Marcus Olvane
Cell: (917) 482-0657
Email: marcus@rkwholdings-example.com
Website: www.rkwholdings-example.com
Address: 418, 9th Street, Brooklyn NY 11218

Colors

Designer to choose colors to be used in the design.

Requirements
Nice to have
• Colors to match logo

```html
<!DOCTYPE html>
<html lang="en">
<head>
<meta charset="utf-8">
<title>RKW Holdings — Business Cards</title>
<link href="https://fonts.googleapis.com/css2?family=Cinzel:wght@400&family=Montserrat:wght@300&family=Roboto:wght@400&display=swap" rel="stylesheet">
<style>
  :root {
    --brand-blue: #1272ad;
    --ink: #3a3a3c;
    --paper: #ffffff;
    --stage: #e9e9ea;
    --mark-faint: #eef3f7;
  }
  * { box-sizing: border-box; margin: 0; padding: 0; }
  html, body { width: 1200px; height: 716px; overflow: hidden; }
  body {
    background: var(--stage);
    position: relative;
    font-family: "Roboto", Arial, sans-serif;
  }
  .card {
    position: absolute;
    top: 203px;
    width: 540px;
    height: 309px;
    box-shadow: 0 6px 18px rgba(0,0,0,.18);
    overflow: hidden;
  }
  /* Front */
  .card--front { left: 40px; background: var(--brand-blue); color: var(--paper); }
  .front-brand {
    position: absolute; left: 0; right: 0; top: 84px;
    display: flex; flex-direction: column; align-items: center;
  }
  .front-brand__square {
    width: 46px; height: 46px; background: var(--paper); margin-bottom: 18px;
  }
  .front-brand__name {
    font-family: "Cinzel", "Times New Roman", serif;
    font-size: 34px; letter-spacing: 1px; color: var(--paper);
  }
  .front-brand__tagline {
    margin-top: 12px;
    font-family: "Montserrat", Arial, sans-serif;
    font-weight: 300; font-size: 13px; letter-spacing: 2px;
  }
  /* Back */
  .card--back { left: 620px; background: var(--paper); color: var(--ink); }
  .back-mark {
    position: absolute; right: -40px; bottom: -50px;
    width: 210px; height: 210px;
    border: 26px solid var(--mark-faint);
  }
  .back-brand {
    position: absolute; left: 150px; top: 34px;
    display: flex; align-items: center; gap: 14px;
  }
  .back-brand__square { width: 30px; height: 30px; background: var(--brand-blue); }
  .back-brand__name {
    font-family: "Cinzel", "Times New Roman", serif;
    font-size: 24px; color: var(--brand-blue);
  }
  .person { position: absolute; left: 44px; top: 112px; }
  .person__name {
    font-family: "Cinzel", "Times New Roman", serif;
    font-size: 22px; color: var(--brand-blue); line-height: 1;
  }
  .person__title { font-size: 13px; margin-top: 5px; color: var(--ink); }
  .contacts { position: absolute; left: 44px; top: 176px; list-style: none; }
  .contacts li {
    display: flex; align-items: center; gap: 7px;
    font-size: 12.5px; line-height: 20px;
  }
  .contacts .accent { color: var(--brand-blue); }
  .icon { width: 11px; height: 11px; fill: var(--brand-blue); flex: none; }
  .address {
    position: absolute; right: 40px; bottom: 36px;
    display: flex; gap: 7px; font-size: 13px; line-height: 18px;
  }
  .address .icon { margin-top: 3px; }
</style>
</head>
<body>
  <section class="card card--front" aria-label="Card front">
    <div class="front-brand">
      <div class="front-brand__square"></div>
      <div class="front-brand__name">RKW Holdings</div>
      <div class="front-brand__tagline">Real Estate Investment Fund</div>
    </div>
  </section>

  <section class="card card--back" aria-label="Card back">
    <div class="back-mark"></div>
    <div class="back-brand">
      <div class="back-brand__square"></div>
      <div class="back-brand__name">RKW Holdings</div>
    </div>
    <div class="person">
      <div class="person__name">MARCUS OLVANE</div>
      <div class="person__title">Managing Director</div>
    </div>
    <ul class="contacts">
      <li>
        <svg class="icon" viewBox="0 0 24 24"><path d="M6.6 10.8a15.1 15.1 0 0 0 6.6 6.6l2.2-2.2a1 1 0 0 1 1-.25 11.4 11.4 0 0 0 3.6.57 1 1 0 0 1 1 1V20a1 1 0 0 1-1 1A17 17 0 0 1 3 4a1 1 0 0 1 1-1h3.5a1 1 0 0 1 1 1c0 1.25.2 2.45.57 3.57a1 1 0 0 1-.25 1z"/></svg>
        (917) 482-0657
      </li>
      <li>
        <svg class="icon" viewBox="0 0 24 24"><path d="M2 5h20v14H2z M2 5l10 8 10-8" fill="none" stroke="#1272ad" stroke-width="2.4"/></svg>
        marcus@rkwholdings-example.com
      </li>
      <li>
        <svg class="icon" viewBox="0 0 24 24"><circle cx="12" cy="12" r="10"/></svg>
        <span>www.<span class="accent">rkwholdings-example</span>.com</span>
      </li>
    </ul>
    <div class="address">
      <svg class="icon" viewBox="0 0 24 24"><path d="M12 2a7 7 0 0 0-7 7c0 5 7 13 7 13s7-8 7-13a7 7 0 0 0-7-7zm0 9.5A2.5 2.5 0 1 1 12 6.5a2.5 2.5 0 0 1 0 5z"/></svg>
      <div>418, 9th Street,<br>Brooklyn NY 11218</div>
    </div>
  </section>
</body>
</html>
```